BKT Business Card

Business card design for a handyman company. Want to portray a professional image and stay away from the "Mom & Pops" image that is normally associated with handyman companies.

```html
<!DOCTYPE html>
<html lang="en">
<head>
<meta charset="utf-8">
<title>BKT Business Card</title>
<link rel="stylesheet" href="https://fonts.googleapis.com/css2?family=Arimo:wght@700&family=Saira+Semi+Condensed:wght@600&display=swap">
<style>
  :root {
    --ink-navy: #0e2440;
    --card-white: #ffffff;
    --blue-light: #c9ccff;
    --blue-mid: #5a5cf0;
    --blue-deep: #2a2ad4;
    --text-white: #ffffff;
  }
  html, body {
    margin: 0;
    padding: 0;
    width: 1200px;
    height: 685px;
    overflow: hidden;
    background: var(--card-white);
  }
  .business-card {
    position: relative;
    width: 1200px;
    height: 685px;
    overflow: hidden;
    background: linear-gradient(180deg,
      var(--card-white) 0%,
      var(--card-white) 36%,
      var(--blue-light) 52%,
      var(--blue-mid) 70%,
      var(--blue-deep) 100%);
  }
  .brand-name {
    position: absolute;
    left: 0;
    right: 0;
    top: 40px;
    margin: 0;
    text-align: center;
    font-family: "Saira Semi Condensed", sans-serif;
    font-weight: 600;
    color: var(--ink-navy);
    line-height: 1;
  }
  .brand-name .brand-main {
    display: block;
    font-size: 190px;
    letter-spacing: 4px;
  }
  .brand-name .brand-sub {
    display: block;
    margin-top: 38px;
    font-size: 62px;
    letter-spacing: 12px;
  }
  .service-scope {
    position: absolute;
    left: 0;
    right: 0;
    top: 352px;
    margin: 0;
    text-align: center;
    font-family: "Saira Semi Condensed", sans-serif;
    font-weight: 600;
    font-size: 56px;
    color: var(--ink-navy);
    letter-spacing: 0.5px;
  }
  .contact-list,
  .service-list {
    position: absolute;
    top: 438px;
    margin: 0;
    padding: 0;
    list-style: none;
    font-family: "Arimo", sans-serif;
    font-weight: 700;
    font-size: 32px;
    line-height: 44.5px;
    color: var(--text-white);
  }
  .contact-list { left: 38px; }
  .service-list { right: 38px; text-align: right; }
  .contact-email {
    position: absolute;
    left: 0;
    right: 0;
    top: 620px;
    margin: 0;
    padding-right: 280px;
    text-align: center;
    font-family: "Arimo", sans-serif;
    font-weight: 700;
    font-size: 30px;
    letter-spacing: 1px;
    color: var(--text-white);
  }
</style>
</head>
<body>
  <main class="business-card">
    <h1 class="brand-name">
      <span class="brand-main">Brightkeep</span>
      <span class="brand-sub">Trades</span>
    </h1>
    <p class="service-scope">Residential &amp; Commercial Services</p>
    <ul class="contact-list">
      <li>470 W Elm St</li>
      <li>Millbrook, Ks 66500</li>
      <li>(555) 014-7720 p</li>
      <li>(555) 014-7721 f</li>
    </ul>
    <ul class="service-list">
      <li>Home Repairs</li>
      <li>Handyman Services</li>
      <li>Drain Cleaning</li>
      <li>Carpet Cleaning</li>
    </ul>
    <p class="contact-email">info@BrightkeepTrades.com</p>
  </main>
</body>
</html>
```